Life and Personal development life coach needs card design

I need a card design that matches the style and design of my website. I'd like to stay in the same color scheme. Please check out my website for ideas. www.brivelmorcott.com
I have had previous designs for this. I am wondering if you have access to those for more ideas??

```html
<!DOCTYPE html>
<html lang="en">
<head>
<meta charset="utf-8">
<title>Maren Colwell, RN – Life Coach Business Card</title>
<link rel="stylesheet" href="https://fonts.googleapis.com/css2?family=Cinzel:wght@400;500&family=Arimo:wght@400&family=Parisienne&display=swap">
<style>
  :root {
    --page: #ffffff;
    --card: #ffffff;
    --frame: #7b9a31;
    --accent: #7f9e35;
    --ink: #111111;
    --badge-blue: #8fb2d8;
    --badge-cream: #e9e3cf;
    --badge-slate: #9aa6b4;
  }
  html, body {
    margin: 0;
    padding: 0;
    width: 1200px;
    height: 1194px;
    overflow: hidden;
    background: var(--page);
  }
  .canvas {
    position: relative;
    width: 1200px;
    height: 1194px;
  }
  .card {
    position: absolute;
    left: 375px;
    width: 522px;
    height: 338px;
    box-sizing: border-box;
    border: 11px solid var(--frame);
    background: var(--card);
    text-align: center;
    color: var(--ink);
    overflow: hidden;
  }
  .card--front { top: 246px; }
  .card--back { top: 626px; }

  .front__kicker {
    position: absolute;
    top: 84px;
    left: 0; right: 0;
    margin: 0;
    font-family: "Cinzel", serif;
    font-size: 15px;
    letter-spacing: 0.2px;
  }
  .front__title {
    position: absolute;
    top: 104px;
    left: 0; right: 0;
    margin: 0;
    font-family: "Cinzel", serif;
    font-weight: 500;
    font-size: 62px;
    line-height: 1;
    letter-spacing: 1px;
  }
  .front__tagline {
    position: absolute;
    top: 193px;
    left: 0; right: 0;
    margin: 0;
    font-family: "Arimo", sans-serif;
    font-size: 15px;
  }
  .front__motto {
    position: absolute;
    top: 214px;
    left: 0; right: 0;
    margin: 0;
    font-family: "Parisienne", cursive;
    font-size: 21px;
    color: var(--accent);
  }

  .back__name {
    position: absolute;
    top: 86px;
    left: 0; right: 0;
    margin: 0;
    font-family: "Arimo", sans-serif;
    font-size: 31px;
    font-weight: 400;
  }
  .back__role {
    position: absolute;
    top: 129px;
    left: 0; right: 0;
    margin: 0;
    font-family: "Arimo", sans-serif;
    font-size: 25px;
    color: var(--accent);
  }
  .back__email {
    position: absolute;
    top: 170px;
    left: 0; right: 0;
    margin: 0;
    font-family: "Arimo", sans-serif;
    font-size: 21px;
  }
  .back__badges {
    position: absolute;
    left: 0;
    top: 212px;
    display: block;
  }
</style>
</head>
<body>
<main class="canvas">
  <section class="card card--front">
    <p class="front__kicker">TRANSFORMATION AND PERSONAL DEVELOPMENT</p>
    <h1 class="front__title">LIFE COACH</h1>
    <p class="front__tagline">Health, Strength &amp; Balancefor Your Mind and Soul</p>
    <p class="front__motto">Discover a life without limits!</p>
  </section>

  <section class="card card--back">
    <h2 class="back__name">Maren Colwell, RN</h2>
    <p class="back__role">Tranformational Life Coach</p>
    <p class="back__email">maren@brivelmorcott.com</p>
    <svg class="back__badges" width="500" height="96" viewBox="0 0 500 96" aria-hidden="true">
      <rect class="badge badge--association" x="22" y="18" width="134" height="58" rx="4" fill="var(--badge-blue)" opacity="0.75"/>
      <circle class="badge badge--certificate" cx="260" cy="48" r="40" fill="var(--badge-cream)"/>
      <circle class="badge badge--method" cx="428" cy="48" r="42" fill="var(--badge-slate)"/>
    </svg>
  </section>
</main>
</body>
</html>
```